Business card for utility of the future

I need a business card template designed for brookvane. We provide sustainable water, energy and waste services to homes.

The card should include name, position, email address, phone number, website and our logo (attached). I would like it to convey professionalism and creativity.

Target Market(s)

Homeowners, investors, corporate partners.

Industry/Entity Type

Utility

Contact Information for Business Card

The card should include name, position, email address, phone number, website and our logo (attached).

```html
<!DOCTYPE html>
<html lang="en">
<head>
<meta charset="UTF-8">
<title>brookvane — Business Card</title>
<link href="https://fonts.googleapis.com/css2?family=Montserrat:wght@500;600;700;800&display=swap" rel="stylesheet">
<style>
  :root {
    --backdrop: #e2e4e5;
    --brand-green: #6cc285;
    --card-white: #ffffff;
    --text-green: #5fb97a;
    --icon-fg: #ffffff;
  }
  * { margin: 0; padding: 0; box-sizing: border-box; }
  html, body {
    width: 1200px;
    height: 800px;
    overflow: hidden;
    background: var(--backdrop);
    font-family: "Montserrat", Arial, sans-serif;
  }
  .canvas {
    width: 1200px;
    height: 800px;
    display: flex;
    align-items: center;
    justify-content: center;
    gap: 40px;
  }
  .card {
    width: 540px;
    height: 309px;
    border-radius: 24px;
    position: relative;
    box-shadow: 0 10px 30px rgba(0,0,0,0.10);
  }
  .card--front {
    background: var(--brand-green);
    display: flex;
    align-items: center;
    justify-content: center;
  }
  .wordmark {
    font-weight: 800;
    letter-spacing: 0.5px;
    line-height: 1;
  }
  .card--front .wordmark {
    color: var(--card-white);
    font-size: 44px;
  }
  .card--back {
    background: var(--card-white);
  }
  .card--back .wordmark {
    position: absolute;
    top: 34px;
    right: 36px;
    color: var(--text-green);
    font-size: 40px;
  }
  .holder {
    position: absolute;
    left: 36px;
    bottom: 38px;
    color: var(--text-green);
  }
  .holder__name {
    font-size: 21px;
    font-weight: 700;
    letter-spacing: 2px;
  }
  .holder__role {
    font-size: 12px;
    font-weight: 600;
    letter-spacing: 1px;
    margin-top: 2px;
  }
  .contacts {
    position: absolute;
    right: 36px;
    bottom: 100px;
    list-style: none;
    color: var(--text-green);
    font-size: 11.5px;
    font-weight: 500;
    letter-spacing: 0.8px;
  }
  .contacts__item {
    display: flex;
    align-items: center;
    gap: 9px;
    margin-top: 5px;
  }
  .contacts__icon {
    width: 15px;
    height: 15px;
    flex: none;
  }
</style>
</head>
<body>
<main class="canvas">
  <section class="card card--front" aria-label="Card front">
    <span class="wordmark">brookvane</span>
  </section>

  <section class="card card--back" aria-label="Card back">
    <span class="wordmark">brookvane</span>

    <ul class="contacts">
      <li class="contacts__item">
        <svg class="contacts__icon" viewBox="0 0 16 16" aria-hidden="true">
          <circle cx="8" cy="8" r="8" fill="var(--brand-green)"/>
          <path d="M5.2 4.2c.4-.3.9-.2 1.1.2l.6 1.2c.2.4.1.8-.2 1l-.5.4c.4.9 1.1 1.6 2 2l.4-.5c.3-.3.7-.4 1-.2l1.2.6c.4.2.5.7.2 1.1l-.5.6c-.4.4-1 .5-1.5.3-2-.8-3.5-2.3-4.3-4.3-.2-.5-.1-1.1.3-1.5z" fill="var(--icon-fg)"/>
        </svg>
        <span>123 . 456 . 789</span>
      </li>
      <li class="contacts__item">
        <svg class="contacts__icon" viewBox="0 0 16 16" aria-hidden="true">
          <circle cx="8" cy="8" r="8" fill="var(--brand-green)"/>
          <rect x="4" y="5.2" width="8" height="5.6" rx="0.8" fill="none" stroke="var(--icon-fg)" stroke-width="1.1"/>
          <path d="M4.3 5.6 8 8.4l3.7-2.8" fill="none" stroke="var(--icon-fg)" stroke-width="1.1"/>
        </svg>
        <span>johndoe@company.com</span>
      </li>
      <li class="contacts__item">
        <svg class="contacts__icon" viewBox="0 0 16 16" aria-hidden="true">
          <circle cx="8" cy="8" r="8" fill="var(--brand-green)"/>
          <circle cx="8" cy="8" r="3.8" fill="none" stroke="var(--icon-fg)" stroke-width="1"/>
          <ellipse cx="8" cy="8" rx="1.6" ry="3.8" fill="none" stroke="var(--icon-fg)" stroke-width="1"/>
          <path d="M4.2 8h7.6" stroke="var(--icon-fg)" stroke-width="1"/>
        </svg>
        <span>www.yourcompany.com</span>
      </li>
    </ul>

    <div class="holder">
      <p class="holder__name">John Doe</p>
      <p class="holder__role">Manager</p>
    </div>
  </section>
</main>
</body>
</html>
```